Meridian Fiscal Outreach Summit Web Page Banner

I would like a banner with Conference Logo and Pictures from previous conferences, fading in and out whilst the logo remain stationery. Pictures of people, patients, doctors, community, hospital. Financial initiative conference of health service providers. Financing is essential to healthcare, hence ways of improving healthcare at the same time making it more affordable to the patients is the primary objective for the Conference.

Target Market(s)

Financial Health Services

Industry/Entity Type

Financial

Number of Pages Required

1 page

Colors
0492cd
ffc214
ec1f27
9bcb3b
e34197
0392cd

Requirements
Must have
• This banner should fit into one of Wordpress, themes. I will send the person the theme that is being used to ensure it fits with the site.

```html
<!DOCTYPE html>
<html lang="en">
<head>
<meta charset="utf-8">
<title>Meridian Fiscal Outreach Summit 2015</title>
<link href="https://fonts.googleapis.com/css2?family=Arimo:wght@400;700&family=Open+Sans:wght@400;600&display=swap" rel="stylesheet">
<style>
:root{
  --blue:#0492cd;
  --yellow:#ffc214;
  --red:#ec1f27;
  --green:#9bcb3b;
  --pink:#e34197;
  --dropdown:#fde7f1;
  --ink:#222;
  --panel:#e6e6e6;
  --footer:#3a3a3a;
  --footer-line:#5a5a5a;
  --gold-link:#f2b51b;
  --thumb-frame:#d79aa3;
}
*{box-sizing:border-box;margin:0;padding:0}
html,body{width:800px;height:1200px;overflow:hidden;background:#fff}
body{position:relative;font-family:"Arimo",Arial,sans-serif;color:var(--ink)}
.abs{position:absolute}

/* header */
.account{left:589px;top:19px;font-size:11px;font-weight:700;color:#333;display:flex;gap:14px}
.search{left:681px;top:17px;width:101px;height:17px;border:2px solid #888;display:flex;background:#fff}
.search span{flex:1;font-size:10px;color:#aaa;padding:1px 5px}
.search i{width:24px;background:#b9d7e8;display:flex;align-items:center;justify-content:center}
.brand{left:15px;top:40px;display:flex;align-items:flex-start;gap:8px}
.brand-dot{width:46px;height:46px;border-radius:50%;background:var(--blue);margin-top:2px}
.brand-name{font-size:13px;font-weight:700;color:#222;line-height:15px;width:150px;text-transform:uppercase}
.brand-place{left:69px;top:90px;font-size:5.5px;font-weight:700;color:var(--pink);letter-spacing:.2px}
.nav{left:269px;top:111px;font-size:9.5px;font-weight:700;color:#333;letter-spacing:.2px;display:flex;gap:6px;white-space:nowrap}
.nav .active{color:var(--pink)}
.nav .sep{font-weight:400}
.dropdown{left:604px;top:125px;width:183px;height:37px;background:var(--dropdown);font-size:8.5px;font-weight:700;color:#333;padding:2px 7px;line-height:15px;white-space:nowrap;z-index:3}
.bar{top:135px;height:23px}

/* hero */
.hero{left:0;top:162px;width:800px;height:389px;background:linear-gradient(150deg,#070707 0%,#123c44 35%,#1d8494 50%,#6e6a22 68%,#1c1c10 85%,#060606 100%)}
.arrow{top:342px;width:31px;height:31px}
.hero-title{left:65px;top:452px;font-size:36px;font-weight:700;color:#fff;line-height:41px;text-shadow:2px 2px 4px rgba(0,0,0,.6)}

/* promo tiles */
.tile{top:565px;width:187px;height:107px;display:flex;align-items:center;padding:0 10px;gap:8px}
.tile p{font-size:8.5px;font-weight:700;line-height:12px;width:76px;color:#222}
.tile .photo{width:88px;height:59px;background:linear-gradient(135deg,#6a5a4a,#c7b8a6 60%,#3d3a3c)}
.t1{left:9px;background:var(--yellow)}
.t2{left:207px;background:var(--blue)}
.t3{left:405px;background:var(--green)}
.t4{left:604px;background:var(--pink)}

/* info columns */
.info{top:683px;width:184px;height:260px;background:var(--panel);padding:7px 6px}
.info h2{background:var(--red);color:#fff;font-size:11px;font-weight:700;text-align:center;height:24px;line-height:24px;margin-bottom:12px}
.info p{font-size:7.6px;font-weight:700;line-height:11px;padding:0 4px;margin-bottom:9px}
.info1{left:11px}
.info2{left:207px}
.article{left:405px;width:232px}
.article h3{font-size:10.5px;font-weight:400;color:var(--red);margin-bottom:3px}
.article p{font-size:7.8px;line-height:11.6px;text-align:justify;color:#333}
.a1{top:681px}
.a2{top:825px}
.art{left:640px;width:141px;height:100px}
.art-health{top:698px;background:linear-gradient(135deg,#f4f4f6,#e3dcef 55%,#d9eef3)}
.art-finance{top:843px;background:linear-gradient(135deg,#f6f6f6,#f3e6d6 55%,#dfe8f4)}

/* footer */
.footer{left:0;top:987px;width:800px;height:213px;background:var(--footer)}
.label{font-family:"Open Sans",Arial,sans-serif;font-size:14px;color:#fff}
.thumb{top:1005px;width:122px;height:72px;border:3px solid var(--thumb-frame);background:linear-gradient(135deg,#2a2420,#8a7a64 55%,#3c3430)}
.play{position:absolute;left:50%;top:50%;width:30px;height:30px;margin:-15px 0 0 -15px}
.rule{left:5px;width:795px;height:1px;background:var(--footer-line)}
.btn{left:19px;width:75px;height:25px;font-family:"Open Sans",Arial,sans-serif;font-size:13px;text-align:center;line-height:25px;color:#222}
.btn-about{top:1101px;background:var(--yellow)}
.btn-support{top:1140px;background:var(--pink)}
.links{left:106px;font-size:9.5px;color:var(--gold-link);letter-spacing:.2px;white-space:nowrap}
.social{top:1140px;width:24px;height:24px}
.copy{left:21px;top:1180px;font-size:8px;color:#fff}
</style>
</head>
<body>

<header>
  <div class="abs account"><span>Login</span><span>Register</span></div>
  <div class="abs search"><span>Search</span>
    <i><svg width="14" height="14" viewBox="0 0 14 14"><circle cx="5.5" cy="5.5" r="4" fill="none" stroke="#1f6fa3" stroke-width="2"/><line x1="8.5" y1="8.5" x2="13" y2="13" stroke="#1f6fa3" stroke-width="2.4"/></svg></i>
  </div>
  <div class="abs brand">
    <div class="brand-dot"></div>
    <div class="brand-name">Meridian Fiscal Outreach Summit 2015</div>
  </div>
  <div class="abs brand-place">PORT ALDER, MERIDIAN ISLES</div>

  <nav class="abs nav">
    <span>HOME</span><span class="sep">|</span><span>ABOUT US</span><span class="sep">|</span><span>PRESENTATIONS</span><span class="sep">|</span><span>PROGRAMME</span><span class="sep">|</span><span>SPEAKERS</span><span class="sep">|</span><span class="active">CONFERENCE</span><span class="sep">|</span><span>CONTACTS</span>
  </nav>
  <div class="abs dropdown">9TH CONFERENCE DEBRIEFING NOTES<br>SPONSORS</div>

  <div class="abs bar" style="left:0;width:156px;background:var(--blue)"></div>
  <div class="abs bar" style="left:161px;width:156px;background:var(--yellow)"></div>
  <div class="abs bar" style="left:322px;width:156px;background:var(--red)"></div>
  <div class="abs bar" style="left:483px;width:156px;background:var(--green)"></div>
  <div class="abs bar" style="left:644px;width:156px;background:var(--pink)"></div>
</header>

<section>
  <div class="abs hero" role="img" aria-label="Rippling national flag in aqua, gold and black"></div>
  <svg class="abs arrow" style="left:75px" viewBox="0 0 31 31" aria-label="Previous slide"><circle cx="15.5" cy="15.5" r="13.5" fill="none" stroke="#fff" stroke-width="2.5"/><path d="M18 9 L11 15.5 L18 22 Z" fill="#fff"/></svg>
  <svg class="abs arrow" style="left:685px" viewBox="0 0 31 31" aria-label="Next slide"><circle cx="15.5" cy="15.5" r="13.5" fill="none" stroke="#fff" stroke-width="2.5"/><path d="M13 9 L20 15.5 L13 22 Z" fill="#fff"/></svg>
  <h1 class="abs hero-title">Welcome to 10th Annual<br>Meridian Summit.</h1>
</section>

<section>
  <div class="abs tile t1"><p>Lorem Ipsum is simply dummy text of the printing.</p><div class="photo" role="img" aria-label="Speaker at a podium microphone"></div></div>
  <div class="abs tile t2"><p>Lorem Ipsum is simply dummy text of the printing.</p><div class="photo" role="img" aria-label="Delegates seated at a conference table"></div></div>
  <div class="abs tile t3"><p>Lorem Ipsum is simply dummy text of the printing.</p><div class="photo" role="img" aria-label="Group of delegates standing together"></div></div>
  <div class="abs tile t4"><p>Lorem Ipsum is simply dummy text of the printing.</p><div class="photo" role="img" aria-label="Delegates reading conference papers"></div></div>
</section>

<section>
  <div class="abs info info1">
    <h2>About Meridian Isles</h2>
    <p>Lorem Ipsum is simply dummy text printing.</p>
    <p>Typesetting industry. Lorem Ipsum has been the industry's standard.</p>
    <p>Dummy text ever since the 1500s, when an printer took a galley of type and scrambled.</p>
    <p>Specimen book. It has survived not only five centuries, but also the leap into electronic .</p>
    <p style="margin-top:14px">Remaining essentially unchanged. It was popularised in the 1960s with the release.</p>
    <p style="margin-top:14px">Publishing software like Quillset Composer including versions of Lorem Ipsum.</p>
  </div>
  <div class="abs info info2">
    <h2>Things to Do</h2>
    <p>Lorem Ipsum is simply dummy text printing.</p>
    <p>Typesetting industry. Lorem Ipsum has been the industry's standard.</p>
    <p>Dummy text ever since the 1500s, when an printer took a galley of type and scrambled.</p>
    <p>Specimen book. It has survived not only five centuries, but also the leap into electronic .</p>
    <p style="margin-top:14px">Remaining essentially unchanged. It was popularised in the 1960s with the release.</p>
    <p style="margin-top:14px">Publishing software like Quillset Composer including versions of Lorem Ipsum.</p>
  </div>

  <article class="abs article a1">
    <h3>Headline is come hrere ABout Healcare</h3>
    <p>Lorem Ipsum is simply dummy text of the printing and typesetting industry. Lorem Ipsum has been the industry's standard dummy text ever since the 1500s, when an unknown printer took a galley of type and scrambled it to make a type specimen book. It has survived not only five centuries, but also the leap into electronic typesetting, remaining essentially unchanged. It was popularised in the 1960s with the release of Typemark sheets containing Lorem Ipsum passages, and more recently with desktop publishing software like Quillset Composer including versions of Lorem Ipsum.</p>
  </article>
  <div class="abs art art-health" role="img" aria-label="Illustration of a 3D bar chart with a stethoscope"></div>

  <article class="abs article a2">
    <h3>Headline is come hrere ABoutFinincial</h3>
    <p>Lorem Ipsum is simply dummy text of the printing and typesetting industry. Lorem Ipsum has been the industry's standard dummy text ever since the 1500s, when an unknown printer took a galley of type and scrambled it to make a type specimen book. It has survived not only five centuries, but also the leap into electronic typesetting, remaining essentially unchanged. It was popularised in the 1960s with the release of Typemark sheets containing Lorem Ipsum passages, and more recently with desktop publishing software like Quillset Composer including versions of Lorem Ipsum.</p>
  </article>
  <div class="abs art art-finance" role="img" aria-label="Illustration of a 3D pie chart and bars on report papers"></div>
</section>

<footer>
  <div class="abs footer"></div>
  <div class="abs label" style="left:32px;top:1028px">Gallery</div>
  <div class="abs thumb" style="left:103px" role="img" aria-label="Delegates in conversation at a reception"></div>
  <div class="abs thumb" style="left:247px" role="img" aria-label="Attendees gathered in the conference hall"></div>
  <div class="abs label" style="left:446px;top:1028px">Video</div>
  <div class="abs thumb" style="left:499px" role="img" aria-label="Video still of the conference audience">
    <svg class="play" viewBox="0 0 30 30"><circle cx="15" cy="15" r="13" fill="rgba(255,255,255,.25)" stroke="#fff" stroke-width="2.5"/><path d="M12 9 L21 15 L12 21 Z" fill="#fff"/></svg>
  </div>
  <div class="abs thumb" style="left:640px" role="img" aria-label="Video still of delegates talking">
    <svg class="play" viewBox="0 0 30 30"><circle cx="15" cy="15" r="13" fill="rgba(255,255,255,.25)" stroke="#fff" stroke-width="2.5"/><path d="M12 9 L21 15 L12 21 Z" fill="#fff"/></svg>
  </div>

  <div class="abs rule" style="top:1093px"></div>
  <div class="abs btn btn-about">About us</div>
  <div class="abs links" style="top:1108px">PRESENTATIONS | PROGRAMME | SPEAKERS | CONFERENCE | SITE MAP | CONTACTS</div>
  <div class="abs label" style="left:603px;top:1104px;font-size:11.5px">Follow us on</div>

  <div class="abs rule" style="top:1133px"></div>
  <div class="abs btn btn-support">Support</div>
  <div class="abs links" style="top:1147px">CUSTOMER | SUPPORT | CONTACTS | FEEDBACK | HELP | SITEMAP</div>
  <div class="abs social" style="left:547px;background:#2aa3e0" role="img" aria-label="Social channel one"></div>
  <div class="abs social" style="left:597px;background:#2d5aa5" role="img" aria-label="Social channel two"></div>
  <div class="abs social" style="left:646px;background:#d9412f" role="img" aria-label="Social channel three"></div>
  <div class="abs social" style="left:695px;background:#1c8ad0" role="img" aria-label="Social channel four"></div>

  <div class="abs rule" style="top:1170px"></div>
  <div class="abs copy">Copyright&nbsp; Meridian fiscal outreach summit 2015</div>
</footer>

</body>
</html>
```